Vitamin Company Website Design

Seeking to create a vibrant and professional looking website for a vitamin and health food supplements business.

Morning Hearthstone is a company that develops and sells vitamins and supplements for those following the "paleo" or "caveman" diet. The diet focuses upon eating organic vegetables and meat, like our ancient ancestors.

The website should emphasize health and wellness. A clean and bold design is preferred.

The website should include four sections: a home page, a blog, a community forum and an e-commerce store.

These websites communicate what we would like to look like:

http://www.korvelintask.com/
http://www.plurisgathering.com/
http://www.xqv.com/
http://www.tulifrond.com/
http://opentalkorbit.com/en/
http://tastemerrowcatch.com/
http://findbrimly.org/

Target Market(s)

Health conscious men and women age 25-50

Industry/Entity Type

E-Commerce

Requirements
Must have
• The website must have 4 pages: home page, blog, community forum and online store.

The website must incorporate the company's logo, which is attached.

The company's green logo with the tagline: "Modern Wellness. Prehistoric Wisdom." is the preferred logo.

Please incorporate the other logo graphics where you see fit.
Nice to have
• Ideally, the designer will add images and/or graphics that compliment a website dedicated to health and wellness.

```html
<!DOCTYPE html>
<html lang="en">
<head>
<meta charset="utf-8">
<title>Morning Hearthstone – Home</title>
<link href="https://fonts.googleapis.com/css2?family=Arimo:wght@400;700&display=swap" rel="stylesheet">
<style>
:root{
  --green:#4aa92b;
  --green-light:#7fd14f;
  --green-dark:#2f8a1b;
  --ink:#2b2b2b;
  --body:#444;
  --muted:#8a8a8a;
  --rule:#e3e3e3;
  --panel:#efefef;
  --orange:#d8431c;
  --teal:#1aa6c0;
  --footer-top:#7a7a7a;
  --footer-bottom:#4e4e4e;
  --field:#a9a9a9;
}
*{box-sizing:border-box;margin:0;padding:0}
html,body{width:710px;height:1200px;overflow:hidden;background:#fff}
body{font-family:"Arimo",Arial,sans-serif;color:var(--body);position:relative}
.abs{position:absolute}
/* header */
.brand{left:18px;top:28px;display:flex;align-items:center;gap:10px}
.brand-dot{width:56px;height:56px;border-radius:50%;background:#8c8c8c}
.brand-name{font-size:25px;font-weight:700;color:var(--green);letter-spacing:-.5px}
.search{left:484px;top:74px;width:206px;height:26px;border:3px solid #dcdcdc;background:#fff;font-size:9px;font-style:italic;color:#555;padding:5px 6px}
.search svg{position:absolute;right:4px;top:2px}
/* nav */
.nav{left:0;top:104px;width:710px;height:30px;background:linear-gradient(#8fd95c,var(--green));display:flex;align-items:center}
.nav a{color:#fff;font-size:10px;font-weight:700;text-decoration:none;text-transform:uppercase;padding:0 26px;height:30px;line-height:30px}
.nav a.active{background:var(--green-dark);border:1px solid #247214;width:93px;text-align:center;margin-left:2px;padding:0}
.nav a:nth-child(3){padding-left:28px;padding-right:26px}
/* hero */
.hero{left:14px;top:151px;width:682px;height:220px;background:var(--panel);padding:7px}
.hero-photo{width:100%;height:100%;background:linear-gradient(180deg,#7fa6d8 0%,#cfe0f0 55%,#7fae45 82%,#4f8a28 100%);position:relative}
.hero-shade{position:absolute;right:0;top:0;width:45%;height:82%;background:linear-gradient(90deg,rgba(255,255,255,0),#f4f5f3 40%)}
.hero-title{position:absolute;left:462px;top:58px;font-size:26px;font-weight:700;line-height:1.1}
.hero-title span{display:block}
.hero-title .l1{color:var(--green)}
.hero-title .l2{color:#444;margin-left:48px}
.pager{position:absolute;right:8px;bottom:4px;display:flex;gap:2px}
.pager i{font-style:normal;font-size:8px;color:#fff;background:#6a9a2e;width:11px;height:11px;text-align:center;line-height:11px}
.pager i.on{background:#ddd;color:#333}
.hero-shadow{left:140px;top:368px;width:460px;height:14px;border-radius:50%;box-shadow:0 8px 10px -4px rgba(0,0,0,.35)}
/* posts */
.post{left:13px;width:430px;height:162px;border-bottom:1px solid var(--rule)}
.comments{position:absolute;right:0;top:8px;font-size:7px;color:var(--green);display:flex;gap:4px;align-items:center}
.comments b{width:7px;height:6px;background:#999;display:block}
.thumb{position:absolute;left:24px;top:26px;width:112px;height:92px;background:linear-gradient(135deg,#f4f4f4,#dcdcdc 60%,#c9d7b8);box-shadow:0 1px 3px rgba(0,0,0,.3);border:1px solid #ddd}
.post h2{position:absolute;left:152px;top:26px;font-size:14px;color:var(--ink);font-weight:700}
.post p{position:absolute;left:152px;top:52px;width:274px;font-size:8.5px;line-height:11.3px;color:#444}
.read{position:absolute;left:152px;top:108px;font-size:8.5px;color:var(--green);text-decoration:none}
.paging{left:13px;top:882px;width:430px;height:32px;border-bottom:1px solid var(--rule);font-size:14px;color:#666;padding-left:155px}
.paging b{color:var(--green);margin-left:10px}
/* sidebar */
.rss{left:475px;top:404px;width:44px;height:44px;border-radius:50%;background:radial-gradient(circle at 40% 35%,#ff8c4a,var(--orange))}
.stat{top:405px;font-size:9px;line-height:10px}
.stat strong{display:block;font-size:16px;line-height:18px}
.stat a{font-size:7px;text-decoration:underline}
.stat.readers strong,.stat.readers a{color:var(--orange)}
.stat.followers strong,.stat.followers a{color:var(--teal)}
.stat span{color:#444}
.side-h{left:475px;font-size:13px;font-weight:700;color:var(--green);width:208px;padding-bottom:4px;border-bottom:5px solid var(--rule)}
.video{left:475px;top:510px;width:208px;height:151px;background:#3a3a3a}
.video-screen{height:130px;background:radial-gradient(ellipse at 50% 0%,#d0d0d0,#8a8a8a 45%,#2e2e2e)}
.video-bar{height:21px;background:linear-gradient(#f2f2f2,#c8c8c8);display:flex;align-items:center;gap:5px;padding:0 5px;font-size:6px;color:#333}
.latest{left:475px;width:208px;display:flex;align-items:center;gap:13px;font-size:8.5px;color:#333}
.latest i{width:28px;height:28px;background:#dcdcdc;border:1px solid #e8e8e8;flex:none}
/* footer */
.footer{left:0;top:966px;width:710px;height:185px;background:linear-gradient(var(--footer-top),var(--footer-bottom))}
.foot-brand{left:36px;top:982px;display:flex;align-items:center;gap:8px}
.foot-brand i{width:36px;height:36px;border-radius:50%;background:#e6e6e6}
.foot-brand span{font-size:18px;color:#fff;font-weight:400}
.foot-text{left:38px;top:1022px;width:210px;font-size:8.5px;line-height:16.5px;color:#fff;font-weight:700}
.contact-h{left:478px;top:990px;font-size:13px;font-weight:700;color:#fff}
.field{left:478px;width:159px;background:var(--field);border:1px solid #bdbdbd;border-radius:5px;font-size:8px;font-style:italic;color:#eee;padding:6px 12px}
.send{left:646px;top:1126px;width:44px;height:18px;border-radius:6px;background:#b5b5b5;font-size:8px;color:#eee;text-align:center;line-height:18px}
.legal{top:1164px;font-size:8px;color:#222}
</style>
</head>
<body>

<header>
  <div class="abs brand"><div class="brand-dot"></div><span class="brand-name">Morning Hearthstone</span></div>
  <div class="abs search">Search
    <svg width="22" height="18" viewBox="0 0 22 18"><circle cx="8" cy="7" r="5.5" fill="none" stroke="#111" stroke-width="2"/><line x1="12" y1="11" x2="19" y2="16" stroke="#111" stroke-width="2.5"/></svg>
  </div>
  <nav class="abs nav">
    <a class="active" href="#">Home</a><a href="#">Blog</a><a href="#">Comunity Forum</a><a href="#">Online Story</a>
  </nav>
</header>

<section class="abs hero">
  <div class="hero-photo" role="img" aria-label="Photo of a group of friends jumping for joy on a grassy hill under a blue sky">
    <div class="hero-shade"></div>
    <div class="hero-title"><span class="l1">Healthy Food</span><span class="l2">Healthy Life</span></div>
    <div class="pager"><i class="on">1</i><i>2</i><i>3</i></div>
  </div>
</section>
<div class="abs hero-shadow"></div>

<main>
  <article class="abs post" style="top:402px">
    <div class="comments"><b></b>02 Comments</div>
    <div class="thumb" role="img" aria-label="Product photo of a multivitamin bottle with fresh fruit and vegetables"></div>
    <h2>Pure Clean Skin</h2>
    <p>Lorem ipsum dolor sit amet, consectetur adipiscing elit. Aenean fermentum malesuada orci a commodo. Aenean dapibus urna quis nulla consequat sagittis. Quisque ut ultrices massa. Mauris felis felis, rutrum sit amet vehicula ut, tempus quis lectus. .</p>
    <a class="read" href="#">Read More</a>
  </article>
  <article class="abs post" style="top:564px">
    <div class="comments"><b></b>14 Comments</div>
    <div class="thumb" role="img" aria-label="Product photo of a multivitamin bottle with fresh fruit and vegetables"></div>
    <h2>Food Nutrition for Weak People</h2>
    <p>Lorem ipsum dolor sit amet, consectetur adipiscing elit. Aenean fermentum malesuada orci a commodo. Aenean dapibus urna quis nulla consequat sagittis. Quisque ut ultrices massa. Mauris felis felis, rutrum sit amet vehicula ut, tempus quis lectus. .</p>
    <a class="read" href="#">Read More</a>
  </article>
  <article class="abs post" style="top:724px">
    <div class="comments"><b></b>19 Comments</div>
    <div class="thumb" role="img" aria-label="Product photo of a multivitamin bottle with fresh fruit and vegetables"></div>
    <h2>Get Rid of Difficult Diet Programs</h2>
    <p>Lorem ipsum dolor sit amet, consectetur adipiscing elit. Aenean fermentum malesuada orci a commodo. Aenean dapibus urna quis nulla consequat sagittis. Quisque ut ultrices massa. Mauris felis felis, rutrum sit amet vehicula ut, tempus quis lectus. .</p>
    <a class="read" href="#">Read More</a>
  </article>
  <div class="abs paging">1&nbsp; 2&nbsp; 3&nbsp; 4&nbsp; ....<b>Next</b></div>
</main>

<aside>
  <div class="abs rss"></div>
  <div class="abs stat readers" style="left:540px"><strong>199</strong><span>Readers</span><br><a>Subscribe Now</a></div>
  <div class="abs stat followers" style="left:607px"><strong>129</strong><span>Chirpline</span><br><a>Follow on Chirpline</a></div>

  <h3 class="abs side-h" style="top:476px">VIDEOS</h3>
  <div class="abs video">
    <div class="video-screen" style="position:relative">
      <svg style="position:absolute;left:92px;top:58px" width="26" height="28" viewBox="0 0 26 28"><path d="M2 2 L24 14 L2 26 Z" fill="#e8e8e8" stroke="#bbb"/></svg>
    </div>
    <div class="video-bar">
      <svg width="9" height="9"><path d="M1 0 L9 4.5 L1 9Z" fill="#222"/></svg>
      <div style="width:60px;height:3px;background:#c00"></div>
      <div style="width:6px;height:6px;border-radius:50%;background:#555"></div>
      <span>0:31 / 0:31</span>
      <div style="width:14px;height:8px;background:#888;margin-left:4px"></div>
      <div style="width:14px;height:8px;background:#444"></div>
      <div style="width:14px;height:8px;background:#444"></div>
    </div>
  </div>

  <h3 class="abs side-h" style="top:697px">LATEST POSTS</h3>
  <div class="abs latest" style="top:728px"><i></i>Request a quote form PSD in 3 colors</div>
  <div class="abs latest" style="top:763px"><i></i>Thanksgiving greeting card PSD</div>
  <div class="abs latest" style="top:797px"><i></i>Vintage business card PSD (front &amp; back)</div>
  <div class="abs latest" style="top:832px"><i></i>Free xHTML/CSS website template</div>
  <div class="abs latest" style="top:867px"><i></i>fruit illustration, fresh lemon PSD</div>
</aside>

<footer>
  <div class="abs footer"></div>
  <div class="abs foot-brand"><i></i><span>Morning Hearthstone</span></div>
  <p class="abs foot-text">Lorem ipsum dolor sit amet, consectetur adipiscing elit. Proin ut purus odio, quis rutrum nibh. Etiam nec tellus malesuada odio tincidunt fringilla quis vitae nisi. Lorem ipsum dolor sit amet, consectetur adipiscing elit. Nullam fringilla malesuada convallis. Morbi laoreet volutpat rhoncus.</p>
  <h3 class="abs contact-h">CONTACT US</h3>
  <div class="abs field" style="top:1013px;height:24px">Name</div>
  <div class="abs field" style="top:1042px;height:24px">Email</div>
  <div class="abs field" style="top:1071px;height:70px">Your Message</div>
  <div class="abs send">Send</div>
  <div class="abs legal" style="left:13px">Copyright © 2012&nbsp; All Rights Reserved</div>
  <div class="abs legal" style="left:600px">Powered by Quillpress</div>
</footer>

</body>
</html>
```